Tampa, Florida based Real Estate company Business Cards

Need ideas for real estate business cards
Updates

Need extra days to review

Industry/Entity Type

Real Estate

Contact Information for Business Card

Space for image, space for logo, contact information space

Font styles to use
Sans Serif

Colors

Designer to choose colors to be used in the design.

Requirements
Must have
• Options to have duplicate content on the back of card for a team of agents.

```html
<!DOCTYPE html>
<html lang="en">
<head>
<meta charset="utf-8">
<title>Crestview Homes Business Card</title>
<link href="https://fonts.googleapis.com/css2?family=Maven+Pro:wght@400;600&display=swap" rel="stylesheet">
<style>
  :root {
    --stage: #b2b2b2;
    --paper: #ffffff;
    --navy: #1c194f;
    --icon-grey: #a6a6a6;
  }
  * { margin: 0; padding: 0; box-sizing: border-box; }
  html, body { width: 1000px; height: 1200px; overflow: hidden; }
  body {
    background: var(--stage);
    font-family: "Maven Pro", sans-serif;
    position: relative;
  }
  .card {
    position: absolute;
    left: 50px;
    width: 899px;
    height: 540px;
  }
  .card-front { top: 43px; background: var(--paper); }
  .card-back { top: 616px; background: var(--navy); }

  .brand {
    position: absolute;
    width: 420px;
    top: 262px;
    text-align: center;
    font-family: "Maven Pro", sans-serif;
    font-weight: 600;
    line-height: 1.1;
  }
  .brand-name { font-size: 56px; letter-spacing: 4px; display: block; }
  .brand-sub { font-size: 20px; letter-spacing: 7px; display: block; margin-top: 8px; }
  .card-front .brand { left: 48px; color: var(--navy); }
  .card-back .brand { left: 240px; color: var(--paper); }

  .contact {
    position: absolute;
    left: 583px;
    top: 160px;
    color: var(--navy);
  }
  .contact-name { font-size: 26px; font-weight: 600; line-height: 1.2; }
  .contact-role { font-size: 24px; font-weight: 400; line-height: 1.3; margin-bottom: 10px; }
  .contact-list { list-style: none; }
  .contact-list li {
    display: flex;
    align-items: center;
    font-size: 24px;
    height: 37.5px;
  }
  .contact-icon {
    width: 22px; height: 22px;
    background: var(--icon-grey);
    border-radius: 3px;
    margin-right: 10px;
    flex: none;
    display: flex; align-items: center; justify-content: center;
  }
  .social {
    position: absolute;
    left: 685px;
    top: 454px;
    display: flex;
    gap: 11px;
  }
  .social-square {
    width: 47px; height: 47px;
    background: var(--navy);
    border-radius: 3px;
  }
</style>
</head>
<body>
  <section class="card card-front">
    <div class="brand">
      <span class="brand-name">CRESTVIEW</span>
      <span class="brand-sub">HOMES GULF SHORE</span>
    </div>

    <div class="contact">
      <p class="contact-name">Your Name</p>
      <p class="contact-role">Manager</p>
      <ul class="contact-list">
        <li>
          <span class="contact-icon">
            <svg width="14" height="14" viewBox="0 0 14 14"><path d="M3 1 L5 1 L6 4 L4.5 5.2 Q6 8.5 8.8 9.5 L10 8 L13 9 L13 11 Q12 13 10 13 Q2 11 1 3 Q1 1 3 1 Z" fill="#fff"/></svg>
          </span>123 444 555
        </li>
        <li>
          <span class="contact-icon">
            <svg width="14" height="14" viewBox="0 0 14 14"><path d="M7 13 L3.2 7.5 A4.3 4.3 0 1 1 10.8 7.5 Z" fill="none" stroke="#fff" stroke-width="1.4"/><circle cx="7" cy="5" r="1.5" fill="#fff"/></svg>
          </span>789 Your Street Here
        </li>
        <li>
          <span class="contact-icon">
            <svg width="14" height="14" viewBox="0 0 14 14"><rect x="1.5" y="3" width="11" height="8" fill="none" stroke="#fff" stroke-width="1.2"/><path d="M1.5 3 L7 8 L12.5 3" fill="none" stroke="#fff" stroke-width="1.2"/></svg>
          </span>info@yourname.com
        </li>
        <li>
          <span class="contact-icon">
            <svg width="14" height="14" viewBox="0 0 14 14"><circle cx="7" cy="7" r="5.5" fill="none" stroke="#fff" stroke-width="1.1"/><ellipse cx="7" cy="7" rx="2.4" ry="5.5" fill="none" stroke="#fff" stroke-width="1"/><path d="M1.5 7 H12.5" stroke="#fff" stroke-width="1"/></svg>
          </span>www.yourname.com
        </li>
      </ul>
    </div>

    <div class="social">
      <span class="social-square"></span>
      <span class="social-square"></span>
      <span class="social-square"></span>
    </div>
  </section>

  <section class="card card-back">
    <div class="brand">
      <span class="brand-name">CRESTVIEW</span>
      <span class="brand-sub">HOMES GULF SHORE</span>
    </div>
  </section>
</body>
</html>
```